property investment and development company needs a website

we need a website that looks professional and portrays trust for people looking to us to buy their house or investors looking to invest or joint venture with us.
We are based in the west midlands in the UK.
we deal mainly with residential housing, house to flats conversions, HMO's (houses in multiple ocupancy).
we require the website as a first point of contact with potential sellers, renters and investors so links or contact details that are easy to access or see would be good.
I have had logos designed by a brisk easel member and these can be used as guidance for the colour and style of the site.
Target Market(s)
joint venture investment partners, people looking to sell their house, people looking to rent from us.
Coding
Coded - Design and coding required
Number of Pages Required
3 page
Requirements
Must have
- project a professional appearance
- visable contact details

```html
<!DOCTYPE html>
<html lang="en">
<head>
<meta charset="utf-8">
<title>Harlow Homes — Property Development &amp; Investment</title>
<link rel="stylesheet" href="https://fonts.googleapis.com/css2?family=Tinos:wght@400;700&family=Titillium+Web:wght@400;600;700&display=swap">
<style>
:root{
  --gold:#d2a95c;
  --gold-soft:#dcb978;
  --navy:#2a2e3c;
  --cream:#f3f1e6;
  --ink:#3a3d48;
  --muted:#8a8c93;
  --white:#ffffff;
}
*{box-sizing:border-box;margin:0;padding:0}
html,body{width:1200px;height:4091px;overflow:hidden}
body{font-family:"Titillium Web",Arial,sans-serif;color:var(--ink);background:var(--white);position:relative}
.serif{font-family:"Tinos","Times New Roman",serif;font-weight:400}
section{position:absolute;left:0;width:1200px}

/* hero */
.hero{top:0;height:743px;background:linear-gradient(180deg,#3c4453 0%,#5a5a5c 40%,#6b4e33 62%,#3a4a37 100%);color:var(--white)}
.brand{position:absolute;left:80px;top:26px;display:flex;align-items:center;gap:14px;font-size:26px;font-weight:600;letter-spacing:2px;line-height:1}
.brand-dot{width:30px;height:30px;border-radius:50%;background:var(--gold)}
.main-nav{position:absolute;left:530px;top:30px;width:590px;display:flex;justify-content:space-between;font-size:17px;font-weight:700;letter-spacing:.5px}
.main-nav a{color:var(--white);text-decoration:none}
.nav-rule{position:absolute;left:515px;top:84px;width:605px;height:1px;background:rgba(255,255,255,.7)}
.hero-title{position:absolute;top:318px;width:100%;text-align:center;font-size:60px;line-height:1}
.hero-sub{position:absolute;top:388px;width:100%;text-align:center;font-size:34px;line-height:1}
.hero-line{position:absolute;top:432px;width:100%;text-align:center;font-size:20px}
.search-tabs{position:absolute;top:486px;left:405px;display:flex;gap:46px;font-size:15px;font-weight:700}
.search-tabs span{padding-bottom:6px}
.search-tabs .active{border-bottom:3px solid var(--gold)}
.search{position:absolute;top:537px;left:290px;width:622px;height:51px;background:var(--white);display:flex}
.search input{flex:1;border:0;padding:0 18px;font:inherit;font-size:18px}
.search button{width:92px;border:0;background:var(--gold-soft)}

/* about */
.about{top:743px;height:557px;background:var(--cream)}
.section-title{position:absolute;width:100%;text-align:center;color:var(--gold);font-size:50px;line-height:1}
.about .section-title{top:62px}
.about-intro{position:absolute;top:125px;left:350px;width:500px;text-align:center;font-size:16px;line-height:1.3}
.feature{position:absolute;width:330px}
.feature h3{font-size:23px;font-weight:400;color:var(--ink)}
.feature p{font-size:15px;color:var(--muted);line-height:1.3;margin-top:8px}
.feature.left{left:40px;text-align:right;padding-right:75px}
.feature.right{left:810px;padding-left:75px}
.feature .icon{position:absolute;top:2px;width:44px;height:44px}
.feature.left .icon{right:10px}
.feature.right .icon{left:10px}
.feature hr{border:0;height:2px;width:40px;background:var(--gold);margin-top:6px}
.feature.left hr{margin-left:auto}
.emblem{position:absolute;left:500px;top:232px;width:200px;height:200px;border-radius:50%;background:var(--gold);display:flex;align-items:center;justify-content:center;color:var(--white);font-size:28px;font-weight:600;letter-spacing:2px}

/* listings */
.listings{top:1300px;height:528px;background:var(--white)}
.listings .section-title{top:55px}
.view-all{position:absolute;top:120px;width:100%;text-align:center;font-size:17px}
.cards{position:absolute;top:163px;left:29px;display:flex;gap:13px}
.card{width:276px}
.card-photo{height:237px}
.card-meta{font-size:13px;margin-top:6px;word-spacing:6px}
.card-addr{font-size:13px;line-height:1.25}

/* stats */
.stats{top:1828px;height:180px;background:linear-gradient(90deg,#c99c4c,#dcb674 50%,#c99c4c);display:flex;justify-content:center}
.stat{width:252px;text-align:center;color:var(--white);padding-top:38px}
.stat b{display:block;font-size:50px;line-height:1;font-weight:700}
.stat span{font-size:22px}

/* split panels */
.split{height:463px;display:flex}
.split .photo{width:600px;height:100%}
.split .panel{width:600px;background:var(--navy);color:#c9cbd2;padding:68px 60px 0 57px}
.panel h2{color:var(--gold);font-size:50px;line-height:1;margin-bottom:24px}
.panel p{font-size:16px;line-height:1.3;margin-bottom:16px}
.btn{display:inline-block;background:var(--gold-soft);color:var(--white);font-size:16px;padding:4px 16px;border-radius:3px;margin-top:6px}
.sell{top:2008px}
.invest{top:2471px}
.invest .panel{padding-top:52px}

/* testimonials */
.testimonials{top:2934px;height:600px;background:var(--white)}
.testimonials .section-title{top:60px}
.quote{position:absolute;top:225px;font-size:150px;color:var(--gold);line-height:1}
.portrait{position:absolute;left:500px;top:140px;width:200px;height:200px;border-radius:50%;border:5px solid var(--gold);background:radial-gradient(circle,#8a7a68,#3d342c)}
.testimonial-text{position:absolute;top:388px;left:340px;width:520px;text-align:center;font-size:16px;color:var(--muted);line-height:1.3}
.testimonial-rule{position:absolute;top:472px;left:530px;width:140px;height:2px;background:var(--gold)}
.testimonial-name{position:absolute;top:494px;width:100%;text-align:center;font-size:22px}

/* contact */
.contact{top:3534px;height:557px;background:var(--cream)}
.contact-heading{position:absolute;left:93px;top:58px;color:#2f4a6e;font-size:36px;line-height:1.3}
.contact-rule{position:absolute;left:93px;top:196px;width:80px;height:2px;background:var(--gold)}
.contact-region{position:absolute;left:93px;top:250px;font-size:22px}
.contact-addr{position:absolute;left:93px;top:292px;font-size:14px;line-height:1.3}
.col{position:absolute;top:363px;font-size:16px;line-height:1.9}
.col h4{font-size:22px;font-weight:400;margin-bottom:6px}
.col.touch{left:93px}
.col.sitemap{left:374px;color:var(--muted)}
.col.sitemap h4{color:var(--ink)}
.map{position:absolute;left:650px;top:60px;width:415px;height:415px;border-radius:50%;background:radial-gradient(circle,#ece7dc,#d7d2c4)}
</style>
</head>
<body>

<section class="hero" role="img" aria-label="Modern detached house lit at dusk with landscaped garden steps">
  <div class="brand"><span class="brand-dot"></span>HARLOW HOMES</div>
  <nav class="main-nav"><a href="#">BUY</a><a href="#">SELL</a><a href="#">RENT</a><a href="#">INVEST</a><a href="#">NEWS AND INSIGHTS</a></nav>
  <div class="nav-rule"></div>
  <h1 class="hero-title serif">Be an Investor, a Landlord,</h1>
  <p class="hero-sub serif">and/or find your dream home</p>
  <p class="hero-line">with the most complete source of homes and real estate near you</p>
  <div class="search-tabs"><span class="active">BUY</span><span>RENT</span><span>INVEST</span><span>HOME VALUE</span></div>
  <form class="search"><input type="text" aria-label="Search"><button type="button" aria-label="Search"></button></form>
</section>

<section class="about">
  <h2 class="section-title serif">About Us</h2>
  <p class="about-intro">We are a property development and investment company that have our own portfolio and we are active investors who pride ourselves in expanding our business organically.</p>

  <div class="feature left" style="top:265px">
    <svg class="icon" viewBox="0 0 44 44" fill="none" stroke="#d2a95c" stroke-width="2.5"><ellipse cx="20" cy="10" rx="12" ry="5"/><path d="M8 10v20c0 3 5 5 12 5M32 10v10"/><circle cx="33" cy="31" r="6"/></svg>
    <h3>Data Driven</h3><hr>
    <p>In-depth information on cities, renters and neighborhoods</p>
  </div>
  <div class="feature left" style="top:395px">
    <svg class="icon" viewBox="0 0 44 44" fill="none" stroke="#d2a95c" stroke-width="2.5"><rect x="4" y="6" width="36" height="26"/><path d="M10 26l8-8 6 5 10-10M22 32v6M14 38h16"/></svg>
    <h3>Intelligent Match</h3><hr>
    <p>Personal finance preference, such as growth or income</p>
  </div>
  <div class="emblem">HARLOW</div>
  <div class="feature right" style="top:265px">
    <svg class="icon" viewBox="0 0 44 44" fill="none" stroke="#d2a95c" stroke-width="2.5"><circle cx="22" cy="24" r="15"/><path d="M22 24V15M18 5h8"/></svg>
    <h3>Sell Faster</h3><hr>
    <p>Sell your property as a performing asset to investors nationwide</p>
  </div>
  <div class="feature right" style="top:395px">
    <svg class="icon" viewBox="0 0 44 44" fill="none" stroke="#d2a95c" stroke-width="2.5"><path d="M5 22L22 7l17 15M10 18v20h24V18"/><circle cx="22" cy="27" r="4"/></svg>
    <h3>Keep Tenants</h3><hr>
    <p>You can sell without having to wait until property is vacant</p>
  </div>
</section>

<section class="listings">
  <h2 class="section-title serif">New Listings</h2>
  <p class="view-all">View all 360 Listings</p>
  <div class="cards">
    <article class="card"><div class="card-photo" role="img" aria-label="Villa with pool at dusk" style="background:linear-gradient(180deg,#3d6ea8,#c89560 60%,#3c8fb8)"></div><p class="card-meta">2 bed 2 bath</p><p class="card-addr">12 Alder Row Unit 4, Smethwick, B66 1AB<br>West Midlands</p></article>
    <article class="card"><div class="card-photo" role="img" aria-label="White modern two storey house" style="background:linear-gradient(180deg,#d9dde0,#6b6f72 55%,#8c8a84)"></div><p class="card-meta">2 bed 2 bath</p><p class="card-addr">12 Alder Row Unit 4, Smethwick, B66 1AB<br>West Midlands</p></article>
    <article class="card"><div class="card-photo" role="img" aria-label="Contemporary house lit at twilight" style="background:linear-gradient(180deg,#4a5670,#8a7a6c 55%,#3a3a3c)"></div><p class="card-meta">2 bed 2 bath</p><p class="card-addr">12 Alder Row Unit 4, Smethwick, B66 1AB<br>West Midlands</p></article>
    <article class="card"><div class="card-photo" role="img" aria-label="Glass fronted home with pool at night" style="background:linear-gradient(180deg,#1e5fa8,#3b86c9 55%,#1f4f80)"></div><p class="card-meta">2 bed 2 bath</p><p class="card-addr">12 Alder Row Unit 4, Smethwick, B66 1AB<br>West Midlands</p></article>
  </div>
</section>

<section class="stats">
  <div class="stat"><b>500</b><span>Homes for sale</span></div>
  <div class="stat"><b>276</b><span>Recently sold</span></div>
  <div class="stat"><b>1</b><span>Foreclosure</span></div>
  <div class="stat"><b>86</b><span>Price reduced</span></div>
</section>

<section class="split sell">
  <div class="photo" role="img" aria-label="Stone and timber house at sunset" style="background:linear-gradient(180deg,#6b5a5a,#b98a6a 35%,#4a4540 70%,#3e4a30)"></div>
  <div class="panel">
    <h2 class="serif">Sell</h2>
    <p>We undertake the necessary market research to evaluate an option that works for all parties involved. We will help guide you to make an informed decision on how to gain the maximum realistic value</p>
    <p>For those looking to achieve a fast and professional sale to experienced investors, we provide an approach that has been proven to work for many others</p>
    <p>If you would like to discuss a property you are looking to sell, then please contact us on 01632 960418</p>
    <span class="btn">Learn More</span>
  </div>
</section>

<section class="split invest">
  <div class="panel">
    <h2 class="serif">Invest</h2>
    <p>We have our own portfolio and we are active investors, so our finger is on the pulse and we are currently looking for residential development investments &amp; commercial to residential conversions in cities or regional centres showing strong growth</p>
    <p>Our experience in the industry enables us to make extremely quick and well-informed decisions. We follow the opportunities that are presented to us as well as sourcing opportunities ourselves. We are happy to work in partnership and within joint ventures and have a proven track record of establishing excellent relationships in these areas.</p>
    <span class="btn">Learn More</span>
  </div>
  <div class="photo" role="img" aria-label="Lit cabin among snowy pines reflected in a lake" style="background:linear-gradient(180deg,#55606a,#2e3a3a 40%,#8a5a30 55%,#1e2226)"></div>
</section>

<section class="testimonials">
  <h2 class="section-title serif">Testimonials</h2>
  <span class="quote serif" style="left:375px">“</span>
  <div class="portrait" role="img" aria-label="Portrait photo of the client"></div>
  <span class="quote serif" style="left:735px">”</span>
  <p class="testimonial-text">Lorem ipsum dolor sit amet, consectetur adipiscing elit, sed do eiusmod tempor incididunt ut labore et dolore magna aliqua. Ut enim ad minim veniam quis nostrud exercitation</p>
  <div class="testimonial-rule"></div>
  <p class="testimonial-name">Clara Benning</p>
</section>

<section class="contact">
  <p class="contact-heading">Contact us on<br>01632 960418</p>
  <div class="contact-rule"></div>
  <p class="contact-region">West Midlands, United Kingdom</p>
  <p class="contact-addr">Lorem ipsum 0000 Avenue<br>UK</p>
  <div class="col touch">
    <h4>Get in touch</h4>
    <b>Website:</b> harlowhomes.co<br>
    <b>Phone:</b> 01632 960418<br>
    <b>Email:</b> Lorem ipsum
  </div>
  <div class="col sitemap">
    <h4>Sitemap</h4>
    Lorem ipsum<br>Lorem ipsum<br>Lorem ipsum
  </div>
  <div class="map" role="img" aria-label="Map of the West Midlands around Birmingham"></div>
</section>

</body>
</html>
```